Brushline Cookout Product Labeling

We need a label design for a new product we are launching. We have developed a cooking bag that will cook your fish or game bird instantly. This is for the everyday fisherman and upland game hunter. This label will be printed on a thin sticker on the front of a Velnex Bag. The Velnex Bag is 9 1/2 x 12 inches. Inside the Velnex Bag is 3 cooking bags.
Target Market(s)
hunters and fishermen
Industry/Entity Type
Cooking
Font styles to use
Sans Serif
Colors
Designer to choose colors to be used in the design.
Requirements
Must have
- It must have "Brushline Cookout" logo. It should have Reed and Ridge. Reed and Ridge is the type of seasoning. It must have a small place on the label for net weight. It must also have the wording "Contains: 3 Individual Cooking Bags Inside.
Nice to have
- I really like a topographical map in the background. I have attached several images with products like that. It could also be cool having the background of the bag with a tiger trout's scales. I attached some images of that too. Some other ideas I thought i have is having a picture of the bird and fish on the bag. There is an GIF attached that has a cool looking fish that did that. There is also an image of a Brovik product that did the same thing.

```html
<!DOCTYPE html>
<html lang="en">
<head>
<meta charset="utf-8">
<title>Brushline Cookout – Cooking Bag Label</title>
<link href="https://fonts.googleapis.com/css2?family=Bebas+Neue&family=Lato:wght@700&display=swap" rel="stylesheet">
<style>
  :root {
    --frame: #3a3a3c;
    --paper: #f4f4f4;
    --ink: #111111;
    --amber: #f6ad45;
    --amber-deep: #c9862c;
  }
  * { margin: 0; padding: 0; box-sizing: border-box; }
  html, body { width: 974px; height: 1200px; overflow: hidden; background: var(--frame); }
  .label {
    position: relative;
    width: 974px;
    height: 1200px;
    background: var(--frame);
  }
  .label__art {
    position: absolute;
    inset: 0;
    width: 974px;
    height: 1200px;
  }
  .brand-name {
    position: absolute;
    left: 214px;
    top: 478px;
    width: 562px;
    text-align: right;
    font-family: "Bebas Neue", "Arial Narrow", sans-serif;
    font-weight: 400;
    font-size: 84px;
    line-height: 1;
    letter-spacing: 0.3px;
    color: var(--ink);
    white-space: nowrap;
  }
  .seasoning {
    position: absolute;
    left: 214px;
    top: 566px;
    width: 562px;
    text-align: right;
    font-family: "Lato", sans-serif;
    font-weight: 700;
    font-size: 20px;
    line-height: 28px;
    letter-spacing: 1px;
    text-transform: uppercase;
    color: var(--ink);
  }
  .contents {
    position: absolute;
    left: 210px;
    top: 762px;
    width: 552px;
    text-align: center;
    font-family: "Lato", sans-serif;
    font-weight: 700;
    font-size: 24px;
    line-height: 34px;
    color: var(--ink);
    text-transform: uppercase;
  }
  .net-weight {
    position: absolute;
    left: 336px;
    top: 878px;
    width: 300px;
    text-align: center;
    font-family: "Lato", sans-serif;
    font-weight: 700;
    font-size: 23px;
    line-height: 34px;
    color: var(--ink);
  }
</style>
</head>
<body>
  <main class="label">
    <svg class="label__art" viewBox="0 0 974 1200" xmlns="http://www.w3.org/2000/svg">
      <rect class="topo-background" x="62" y="62" width="850" height="1074" fill="var(--paper)"
            role="img" aria-label="Grey topographic contour-line map pattern covering the label background"/>
      <polygon class="badge-outline" points="486,148 802,328 802,872 486,1048 166,872 166,328"
               fill="none" stroke="var(--ink)" stroke-width="6"/>
      <polygon class="badge-field" points="486,164 792,340 792,860 486,1032 181,860 181,340"
               fill="var(--amber)" role="img" aria-label="Orange field with faint topographic contour lines"/>
      <rect class="elk-illustration" x="202" y="266" width="460" height="200" rx="4"
            fill="var(--amber-deep)" role="img" aria-label="Silhouette of a bugling bull elk beside mountain peaks"/>
      <rect class="bird-fish-illustration" x="206" y="614" width="524" height="138" rx="4"
            fill="var(--amber-deep)" role="img" aria-label="Silhouette of an upland game bird and a leaping spotted trout"/>
      <line class="rule" x1="210" y1="755" x2="762" y2="755" stroke="var(--ink)" stroke-width="2.5"/>
      <line class="rule" x1="210" y1="838" x2="762" y2="838" stroke="var(--ink)" stroke-width="2.5"/>
    </svg>

    <h1 class="brand-name">Brushline Cookout</h1>
    <p class="seasoning">Reed and Ridge</p>

    <p class="contents">Contains:<br>3 Individual Cooking Bags Inside</p>

    <p class="net-weight">Net Weight<br>75gm oz</p>
  </main>
</body>
</html>
```